Over The Ridge Mediaworks Business Card
Card design
Over The Ridge Mediaworks Business Card -
Creative Brief
Simple
Simon Ashby
Chief Creative Officer
no address
Simon.Ashby@OverTheRidgeMediaworks.example
OverTheRidgeMediaworks.example
I don't have the source files from my logo project yet but will be uploading soon. Meanwhile please go to: http://entries.markcraftstudio.example/contests/over-the-ridge-logo and refer to winning draft #73 (also draft #5) I would like the front of the card to have the red-background logo plus the web address only
The back of the card will have the black-background logo plus all the personal information in white lettering. I would also like to see a version with the white-background logo and black lettering

```html
<!DOCTYPE html>
<html lang="en">
<head>
<meta charset="utf-8">
<title>Over The Ridge Mediaworks Business Card</title>
<link rel="stylesheet" href="https://fonts.googleapis.com/css2?family=Michroma&display=swap">
<style>
  :root {
    --board: #2b2b2b;
    --label: #f2f2f2;
    --card-white: #ffffff;
    --card-red: #c42026;
    --card-black: #1c1c1c;
    --ink: #1a1a1a;
    --ink-soft: #555555;
    --paper-soft: #e6e6e6;
    --accent-red: #c42026;
  }
  * { margin: 0; padding: 0; box-sizing: border-box; }
  html, body { width: 1200px; height: 806px; overflow: hidden; }
  body {
    background: var(--board);
    font-family: "Michroma", "Helvetica Neue", Arial, sans-serif;
    position: relative;
  }
  .card {
    position: absolute;
    width: 499px;
    height: 264px;
    border-radius: 20px;
    overflow: hidden;
    box-shadow: 0 2px 6px rgba(0,0,0,0.5);
  }
  .card svg.swoosh { position: absolute; inset: 0; width: 100%; height: 100%; }
  .card--front-a { left: 72px; top: 43px; background: var(--card-white); }
  .card--front-b { left: 638px; top: 43px; background: var(--card-red); }
  .card--back-a { left: 72px; top: 424px; background: var(--card-white); }
  .card--back-b { left: 638px; top: 424px; background: var(--card-black); }

  .wordmark {
    position: absolute;
    left: 0; right: 0; top: 58px;
    display: flex; justify-content: center; align-items: center; gap: 14px;
  }
  .wordmark__name {
    font-size: 25px; line-height: 1.25; text-align: center;
    text-transform: uppercase; letter-spacing: 1px;
  }
  .wordmark__dot { width: 18px; height: 18px; border-radius: 50%; }
  .card--front-a .wordmark__name { color: var(--ink); }
  .card--front-a .wordmark__dot { background: var(--accent-red); }
  .card--front-b .wordmark__name { color: var(--card-white); }
  .card--front-b .wordmark__dot { background: var(--ink); }

  .web-address {
    position: absolute; left: 0; right: 0; top: 196px;
    text-align: center; font-size: 11px; font-variant: small-caps; letter-spacing: 0.5px;
  }
  .web-rule { position: absolute; left: 140px; width: 220px; top: 188px; height: 1px; }
  .card--front-a .web-address { color: var(--ink-soft); }
  .card--front-a .web-rule { background: linear-gradient(90deg, transparent, #999, transparent); }
  .card--front-b .web-address { color: var(--paper-soft); }
  .card--front-b .web-rule { background: linear-gradient(90deg, transparent, #f3b6b8, transparent); }

  .person { position: absolute; left: 0; right: 0; top: 96px; text-align: center; }
  .person__name { font-size: 21px; color: var(--accent-red); letter-spacing: 1px; }
  .person__title { font-size: 10px; margin-top: 4px; }
  .card--back-a .person__title { color: var(--ink); }
  .card--back-b .person__title { color: var(--paper-soft); }

  .contact-rule { position: absolute; left: 18px; width: 380px; top: 232px; height: 1px; }
  .card--back-a .contact-rule { background: linear-gradient(90deg, #bbb, transparent); }
  .card--back-b .contact-rule { background: linear-gradient(90deg, #777, transparent); }
  .contact {
    position: absolute; left: 22px; top: 239px;
    font-size: 8px; font-variant: small-caps; letter-spacing: 0.4px;
  }
  .contact__sep { margin: 0 6px; }
  .card--back-a .contact { color: var(--ink-soft); }
  .card--back-b .contact { color: #bdbdbd; }

  .board-label {
    position: absolute; width: 499px; text-align: center;
    color: var(--label); font-size: 20px; font-variant: small-caps; letter-spacing: 1.5px;
  }
</style>
</head>
<body>
  <section class="card card--front-a">
    <svg class="swoosh" viewBox="0 0 499 264" aria-hidden="true">
      <path d="M350 0 Q470 25 499 190 L499 0 Z" fill="#c42026"/>
      <path d="M350 0 Q470 25 499 190" fill="none" stroke="#1a1a1a" stroke-width="3"/>
      <path d="M0 140 Q25 240 160 264 L0 264 Z" fill="#c42026"/>
      <path d="M0 140 Q25 240 160 264" fill="none" stroke="#1a1a1a" stroke-width="3"/>
    </svg>
    <div class="wordmark">
      <span class="wordmark__name">Over The Ridge<br>Mediaworks</span>
      <span class="wordmark__dot"></span>
    </div>
    <div class="web-rule"></div>
    <p class="web-address">OverTheRidgeMediaworks.example</p>
  </section>

  <section class="card card--front-b">
    <svg class="swoosh" viewBox="0 0 499 264" aria-hidden="true">
      <path d="M350 0 Q470 25 499 190 L499 0 Z" fill="#1c1c1c"/>
      <path d="M350 0 Q470 25 499 190" fill="none" stroke="#ffffff" stroke-width="2"/>
      <path d="M0 140 Q25 240 160 264 L0 264 Z" fill="#1c1c1c"/>
      <path d="M0 140 Q25 240 160 264" fill="none" stroke="#ffffff" stroke-width="2"/>
    </svg>
    <div class="wordmark">
      <span class="wordmark__name">Over The Ridge<br>Mediaworks</span>
      <span class="wordmark__dot"></span>
    </div>
    <div class="web-rule"></div>
    <p class="web-address">OverTheRidgeMediaworks.example</p>
  </section>

  <p class="board-label" style="left:72px; top:346px;">Business Card Front A</p>
  <p class="board-label" style="left:638px; top:346px;">Business Card Front B</p>

  <section class="card card--back-a">
    <div class="person">
      <p class="person__name">Simon Ashby</p>
      <p class="person__title">Chief Creative Officer</p>
    </div>
    <div class="contact-rule"></div>
    <p class="contact">310 555 0148<span class="contact__sep">|</span>Simon.Ashby@OverTheRidgeMediaworks.example</p>
  </section>

  <section class="card card--back-b">
    <div class="person">
      <p class="person__name">Simon Ashby</p>
      <p class="person__title">Chief Creative Officer</p>
    </div>
    <div class="contact-rule"></div>
    <p class="contact">310 555 0148<span class="contact__sep">|</span>Simon.Ashby@OverTheRidgeMediaworks.example</p>
  </section>

  <p class="board-label" style="left:72px; top:752px;">Business Card Back A</p>
  <p class="board-label" style="left:638px; top:752px;">Business Card Back B</p>
</body>
</html>
```